依頼詳細
小学校経由で小学生の皆さんに、チラシを配布いたします。岬野市、岬野市教育委員会の後援もとっており、夏休みの宿題対策ワークショップをするどのショッピングセンターよりも選んでいただける、楽しい見栄えの作品になればうれしいです。
記載項目
詳細は添付ファイルにて
サイズ
A4
ページ数
片面
希望イメージ
シンプル 複雑
単色 カラフル
暗い 明るい
日常 高級
遊び心 厳粛
未来的 伝統的
女性的 男性的
希望する色
黄・オレンジ系、青系、水色系
納品ファイル
• 高解像度JPG (.jpg)
• イラストレーター形式 (.ai)
• PNG形式 (.png)
補足説明
■ 選んだ理由

表面のみという表現場所で、内容がみやすく、かつ 大変華やかで
子ども達の目を引くデザインになっているところや、写真のロゴからの抽出で
うまく取り入れていただいたり、気の利いた内容でした

■ 提案者全員のお礼・コメント

たくさんのご応募いただき、まことにありがとうございました。
また、同じくコンペ形式でお世話になると思いますが、ぜひまたご提案ください。
よろしくお願いいたします。

```html
<!DOCTYPE html>
<html lang="ja">
<head>
<meta charset="utf-8">
<title>夏休み 宿題対策ワークショップ</title>
<link href="https://fonts.googleapis.com/css2?family=Dela+Gothic+One&family=M+PLUS+Rounded+1c:wght@500;700;800&display=swap" rel="stylesheet">
<style>
:root{
  --cream:#fffbe3;
  --sun:#ffe97a;
  --orange:#f39a1e;
  --deep-orange:#ea6a12;
  --blue:#1e8fd6;
  --sky:#7fd0f2;
  --pale-sky:#d9f1fb;
  --green:#3db34a;
  --pink:#ec4f8c;
  --purple:#8a5cc4;
  --red:#e8433a;
  --ink:#3a3330;
  --white:#ffffff;
}
*{margin:0;padding:0;box-sizing:border-box}
html,body{width:846px;height:1200px;overflow:hidden}
body{font-family:"M PLUS Rounded 1c",sans-serif;color:var(--ink);background:var(--white)}
.flyer{position:relative;width:846px;height:1200px;overflow:hidden;
  background:radial-gradient(circle at 50% 32%,var(--white) 0,var(--cream) 40%,var(--sun) 100%)}
.art{position:absolute;border-radius:22px}
.art-crafts{left:18px;top:18px;width:230px;height:150px;background:linear-gradient(135deg,#ffd36b,#9fd8f4)}
.art-rocket{left:640px;top:14px;width:190px;height:110px;background:linear-gradient(135deg,#a9e0f5,#ffc66e)}
.art-robot{left:18px;top:290px;width:150px;height:210px;background:linear-gradient(160deg,#9fd8f4,#f7b25a)}
.art-child{left:640px;top:300px;width:190px;height:210px;background:linear-gradient(160deg,#ffd27a,#8fd3f1)}
.badge{position:absolute;left:664px;top:120px;width:150px;height:150px;border-radius:50%;
  background:var(--orange);color:var(--white);display:flex;align-items:center;justify-content:center;
  text-align:center;font-weight:800;font-size:20px;line-height:1.3;border:5px solid var(--white)}
.title{position:absolute;left:0;width:846px;text-align:center;font-family:"Dela Gothic One",sans-serif;
  paint-order:stroke fill;-webkit-text-stroke:10px var(--white);letter-spacing:2px}
.title-summer{top:50px;font-size:62px;color:var(--orange)}
.title-homework{top:130px;font-size:96px;color:var(--green)}
.title-homework .b{color:var(--blue)}
.title-work{top:258px;font-size:108px}
.title-shop{top:372px;font-size:108px}
.c1{color:var(--pink)}.c2{color:var(--orange)}.c3{color:var(--blue)}.c4{color:var(--green)}.c5{color:var(--purple)}.c6{color:var(--red)}
.days{position:absolute;left:30px;top:512px;width:786px;display:flex;gap:14px}
.day{flex:1;background:var(--white);border-radius:18px;border:3px solid var(--sky);padding:58px 10px 10px;position:relative;height:392px}
.day-date{position:absolute;left:50%;top:-34px;transform:translateX(-50%);width:92px;height:92px;border-radius:50%;
  color:var(--white);text-align:center;font-weight:800;display:flex;flex-direction:column;justify-content:center;border:4px solid var(--white)}
.day-date b{font-size:30px;line-height:1}
.day-date span{font-size:16px}
.fri{background:var(--blue)}.sat{background:var(--green)}.sun{background:var(--red)}
.item{display:flex;align-items:center;gap:6px;margin-bottom:8px}
.item-name{font-size:14px;font-weight:700;flex:1}
.price{background:var(--orange);color:var(--white);font-size:13px;font-weight:800;border-radius:20px;padding:2px 9px}
.photo{height:62px;border-radius:10px;margin-bottom:8px}
.p1{background:linear-gradient(135deg,#f6c0d0,#9dd6ef)}
.p2{background:linear-gradient(135deg,#ffe07a,#f3a04a)}
.p3{background:linear-gradient(135deg,#b8e6a8,#7fcdf0)}
.outline{position:absolute;left:30px;top:920px;width:440px;height:262px;background:var(--white);border:3px solid var(--orange);border-radius:14px;padding:44px 14px 10px;font-size:13.5px;line-height:1.6}
.outline h2{position:absolute;left:0;top:0;width:100%;background:var(--orange);color:var(--white);font-size:18px;padding:6px 14px;border-radius:10px 10px 0 0}
.outline .big{font-size:18px;font-weight:800;color:var(--deep-orange)}
.info{position:absolute;left:486px;top:920px;width:330px;font-size:12.5px;border-collapse:collapse}
.info th{width:78px;text-align:left;color:var(--blue);font-weight:800;vertical-align:top;padding:2px 0}
.info td{padding:2px 0;font-weight:700}
.map{position:absolute;left:650px;top:1100px;width:166px;height:82px;background:var(--pale-sky);border-radius:10px;display:flex;align-items:center;justify-content:center;color:var(--blue);font-weight:800}
</style>
</head>
<body>
<main class="flyer">
  <div class="art art-crafts" role="img" aria-label="絵の具パレットと鉛筆、工作道具のイラスト"></div>
  <div class="art art-rocket" role="img" aria-label="鳥とロケットの工作イラスト"></div>
  <div class="art art-robot" role="img" aria-label="段ボールロボットと車の工作イラスト"></div>
  <div class="art art-child" role="img" aria-label="絵を描く子どものイラスト"></div>
  <div class="badge">自由研究や<br>夏の工作に<br>ぴったり!</div>

  <h1>
    <div class="title title-summer">夏休み</div>
    <div class="title title-homework">宿題<span class="b">対策</span></div>
    <div class="title title-work"><span class="c1">ワ</span><span class="c2">ー</span><span class="c3">ク</span></div>
    <div class="title title-shop"><span class="c4">シ</span><span class="c5">ョ</span><span class="c6">ッ</span><span class="c3">プ</span></div>
  </h1>

  <section class="days">
    <div class="day">
      <div class="day-date fri"><b>7/29</b><span>金曜</span></div>
      <div class="item"><span class="item-name">オリジナル傘を作ろう</span><span class="price">300〜</span></div>
      <div class="photo p1" role="img" aria-label="傘の作品写真"></div>
      <div class="item"><span class="item-name">コロコロボール</span><span class="price">300〜</span></div>
      <div class="photo p2" role="img" aria-label="コロコロボールの作品写真"></div>
      <div class="item"><span class="item-name">スクラッチアート</span><span class="price">200〜</span></div>
      <div class="photo p3" role="img" aria-label="スクラッチアートの作品写真"></div>
    </div>
    <div class="day">
      <div class="day-date sat"><b>7/30</b><span>土曜</span></div>
      <div class="item"><span class="item-name">ペットボトルのドレス</span><span class="price">500〜</span></div>
      <div class="photo p3" role="img" aria-label="ペットボトルドレスの作品写真"></div>
      <div class="item"><span class="item-name">ひまわりリース</span><span class="price">300〜</span></div>
      <div class="photo p2" role="img" aria-label="ひまわりリースの作品写真"></div>
      <div class="item"><span class="item-name">風鈴を作ろう</span><span class="price">500〜</span></div>
      <div class="photo p1" role="img" aria-label="風鈴の作品写真"></div>
    </div>
    <div class="day">
      <div class="day-date sun"><b>7/31</b><span>日曜</span></div>
      <div class="item"><span class="item-name">和紙ランタンを作ろう</span><span class="price">300〜</span></div>
      <div class="photo p2" role="img" aria-label="和紙ランタンの作品写真"></div>
      <div class="item"><span class="item-name">走れ!風力カー</span><span class="price">200〜</span></div>
      <div class="item"><span class="item-name">牛乳パックペン立て</span><span class="price">200〜</span></div>
      <div class="photo p1" role="img" aria-label="ペン立ての作品写真"></div>
      <div class="item"><span class="item-name">くるくるランプ</span><span class="price">300〜</span></div>
    </div>
  </section>

  <section class="outline">
    <h2>ワークショップ概要</h2>
    <p>■ 開催日時 <span class="big">7月29日・30日・31日</span></p>
    <p>三日間 午前10時より整理券配布</p>
    <p>(配布場所:セントラルコート)</p>
    <p><span class="big">午前10時〜午後4時ごろまで</span></p>
    <p>※材料がなくなり次第終了とさせていただきます</p>
    <p>■ 参加費 材料費のみ各ブースでお支払い</p>
    <p>■ 参加条件 おひとり様1種目 ※工作見本は会場に展示</p>
  </section>

  <table class="info">
    <tr><th>開催場所</th><td>みさきショッピングパーク<br>Leaf内 セントラルコート<br>(岬野市みどり町 1126-1)</td></tr>
    <tr><th>定　員</th><td>1日15家族</td></tr>
    <tr><th>対　象</th><td>小学生 ※保護者同伴</td></tr>
    <tr><th>運営会社</th><td>株式会社Sunnyway</td></tr>
    <tr><th>問合せ先</th><td>info@sunnyway-event.jp</td></tr>
    <tr><th>主　催</th><td>みさきショッピングパーク Leaf</td></tr>
    <tr><th>後　援</th><td>岬野市、岬野市教育委員会</td></tr>
  </table>
  <div class="map" role="img" aria-label="会場周辺の地図">MAP</div>
</main>
</body>
</html>
```